business card - Helicopter Flight Services, Flight School, etc.

We need a business card design for a new helicopter service.

We offer Helicopter Flight Services, Aerial Filming & Photography, Flight School, and Helicopter Tours. In that order.

Summit Bladecraft, Inc.
Harold Tessendy
SummitBladecraft@Lumenpost.com
303-555-0182

Based at the Coldbrook Airport in Van Nuys, CA. The final design should communicate integrity and safety. Pictures or logos at your discretion.

Card back side - surprise me.

```html
<!DOCTYPE html>
<html lang="en">
<head>
<meta charset="utf-8">
<title>Summit Bladecraft, Inc. — Business Card</title>
<link rel="stylesheet" href="https://fonts.googleapis.com/css2?family=Abril+Fatface&family=Arimo:wght@400&display=swap">
<style>
  :root {
    --page: #ecebe8;
    --card-white: #fbfbfb;
    --card-edge: #2f7bbd;
    --brand-blue: #3a8cc9;
    --ink: #1d1d1d;
    --sky-top: #c9ccd0;
    --sky-mid: #9da3aa;
    --sea: #5d656e;
    --cockpit: #1f2226;
    --white: #ffffff;
  }
  * { margin: 0; padding: 0; box-sizing: border-box; }
  html, body { width: 1200px; height: 892px; overflow: hidden; }
  body {
    background: var(--page);
    display: flex;
    flex-direction: column;
    align-items: center;
    justify-content: center;
    gap: 44px;
    font-family: "Arimo", Arial, sans-serif;
  }
  .card {
    width: 660px;
    height: 377px;
    border: 7px solid var(--card-edge);
    box-shadow: 0 6px 18px rgba(0,0,0,.18);
    position: relative;
    overflow: hidden;
  }
  /* Front */
  .card-front {
    background: linear-gradient(135deg, var(--white) 0%, var(--card-white) 55%, #ececec 100%);
    padding: 46px 0 0 70px;
  }
  .company-name {
    font-family: "Abril Fatface", Georgia, serif;
    font-size: 44px;
    color: var(--brand-blue);
    letter-spacing: .5px;
    line-height: 1;
  }
  .services {
    font-size: 25px;
    color: var(--ink);
    margin: 8px 0 0 68px;
    line-height: 1;
  }
  .rule {
    height: 2px;
    background: var(--ink);
    width: 520px;
    margin: 16px 0 0 38px;
  }
  .person-name {
    font-family: "Abril Fatface", Georgia, serif;
    font-size: 31px;
    color: var(--brand-blue);
    margin: 18px 0 0 160px;
    line-height: 1;
  }
  .contact {
    list-style: none;
    margin: 16px 0 0 70px;
    font-size: 16px;
    color: var(--ink);
    line-height: 1.6;
  }
  .contact li:nth-child(1) { padding-left: 120px; }
  .contact li:nth-child(2) { padding-left: 80px; }
  .contact li:nth-child(3) { padding-left: 40px; }

  /* Back */
  .card-back { background: var(--sea); }
  .cockpit-photo {
    position: absolute; inset: 0;
    background:
      radial-gradient(ellipse 60% 45% at 22% 82%, var(--cockpit) 0%, rgba(31,34,38,.85) 45%, rgba(31,34,38,0) 75%),
      linear-gradient(180deg, var(--sky-top) 0%, var(--sky-mid) 45%, var(--sea) 100%);
  }
  .back-text {
    position: absolute;
    left: 170px; top: 120px;
    color: var(--white);
  }
  .back-text .company-name { color: var(--white); font-size: 46px; }
  .back-text .services { color: var(--white); margin-left: 30px; font-size: 24px; }
</style>
</head>
<body>
  <section class="card card-front" aria-label="Card front">
    <h1 class="company-name">Summit Bladecraft, Inc.</h1>
    <p class="services">Airport · Tour guide · Heliport</p>
    <div class="rule"></div>
    <h2 class="person-name">Harold Tessendy</h2>
    <ul class="contact">
      <li>303-555-0182</li>
      <li>Summit Bladecraft Inc.</li>
      <li>SummitBladecraft@Lumenpost.com</li>
      <li>2284 W. Fernmont Blvd. Ste.A Coldbrook, CA 91599</li>
    </ul>
  </section>

  <section class="card card-back" aria-label="Card back">
    <div class="cockpit-photo" role="img" aria-label="Photo from inside a helicopter cockpit looking out over a grey sea and sky, instrument panel in the lower left"></div>
    <div class="back-text">
      <p class="company-name">Summit Bladecraft, Inc.</p>
      <p class="services">Airport · Tour guide · Heliport</p>
    </div>
  </section>
</body>
</html>
```